Lumo Fortunado superhero master

Full website makeover/update and redesign About a Public Figure.. in Spanish as well as English.
See current website at LumoFortunado.example and Chatterbook page LumoFortunates .
you can use any of the pictures and videos and be creative. page will be in English and Spanish same design.
think about a Zen Superhero, like Kael from the lattice, with secret mystic knowledge, a combination of the character "Captain Vesper" mixed with the Millionaire Falcon of Harbor Row. Themes related to Mentor, based on zodiac, about Financial abundance using the stock Market.

Reason: designs are not what I like

Target Market(s)

USA hispanics Market

Number of Pages Required

5+ page

Colors

Designer to choose colors to be used in the design.

Requirements
Must have
• think about a Zen Superhero, like Kael from the lattice, with secret mystic knowledge, a combination of the character "Captain Vesper" mixed with the Millionaire Falcon of Harbor Row. Themes related to Mentor, based on zodiac, about Financial abundance using the stock Market. Surprise me :)
Nice to have
• think about a Zen Superhero, like Kael from the lattice, with secret mystic knowledge, a combination of the character "Captain Vesper" mixed with the falcon of harbor row.

```html
<!DOCTYPE html>
<html lang="en">
<head>
<meta charset="utf-8">
<title>LumoFortunates</title>
<link rel="stylesheet" href="https://fonts.googleapis.com/css2?family=Jost:wght@400;500;600;700&family=Open+Sans:wght@400;600;700&display=swap">
<style>
:root{
  --green:#2fae4a;
  --red:#e0262b;
  --ink:#222222;
  --muted:#6f6f6f;
  --page:#f4f4f4;
  --white:#ffffff;
  --footer:#2c2c2c;
  --footer-base:#1f1f1f;
  --line:#d9d9d9;
}
*{box-sizing:border-box;margin:0;padding:0}
html,body{width:1200px;height:2479px;overflow:hidden}
body{position:relative;background:var(--page);font-family:"Open Sans",Arial,sans-serif;color:var(--ink)}
.abs{position:absolute}
.heading{font-family:"Jost",Arial,sans-serif;font-weight:600;text-transform:uppercase;letter-spacing:.5px}

/* hero */
.hero{left:0;top:0;width:1200px;height:600px;background:linear-gradient(120deg,#3a3d42 0%,#5b6068 40%,#8a8f96 60%,#2e3035 100%)}
.logo{left:160px;top:36px;display:flex;align-items:center;gap:10px}
.logo-mark{width:14px;height:14px;border-radius:50%;background:var(--white)}
.logo-name{font-family:"Jost",sans-serif;font-weight:600;font-size:26px;color:var(--white);line-height:1}
.nav{right:162px;top:40px;display:flex;gap:8px;align-items:center}
.nav-home{width:30px;height:33px;display:flex;align-items:center;justify-content:center;margin-right:8px}
.nav a{display:block;height:33px;line-height:33px;padding:0 13px;background:var(--white);color:#333;font-family:"Jost",sans-serif;font-size:12px;text-decoration:none;text-transform:uppercase}
.nav a.active{background:var(--green);color:var(--white);padding:0 20px}
.hero-box{left:160px;top:307px;width:478px;height:164px;border:3px solid var(--white);padding:25px 23px}
.hero-title{font-size:27px;line-height:33px;color:var(--white);font-weight:700}
.hero-link{display:inline-block;margin-top:19px;color:var(--white);font-family:"Jost",sans-serif;font-weight:600;font-size:16px;text-decoration:underline}

/* section titles */
.section-title{left:0;width:1200px;text-align:center;font-size:22px;color:var(--ink)}
.section-title em{font-style:normal;color:var(--red)}
.divider{left:566px;width:68px;height:1px;background:#b8b8b8}
.divider::after{content:"";position:absolute;left:31px;top:-2px;width:5px;height:5px;border-radius:50%;background:var(--green)}

.intro{left:230px;top:695px;width:740px;text-align:center;font-size:11.5px;line-height:18px;color:#555}
.btn-outline{left:509px;top:759px;width:177px;height:39px;border:2px solid var(--green);color:var(--green);font-family:"Jost",sans-serif;font-weight:500;font-size:14px;text-transform:uppercase;display:flex;align-items:center;justify-content:center}

/* video feature */
.video{left:160px;top:855px;width:440px;height:277px;background:linear-gradient(160deg,#6c7a6e 0%,#4a5a70 45%,#2e3a2f 100%)}
.video-play{left:186px;top:105px}
.video-caption{left:10px;bottom:10px;color:var(--white);font-family:"Jost",sans-serif;font-weight:600;font-size:15px;letter-spacing:.5px}
.feature{left:600px;top:855px;width:440px;height:277px;background:var(--white);padding:30px 28px;box-shadow:0 10px 16px -12px rgba(0,0,0,.35)}
.feature-title{font-size:17px;letter-spacing:0;color:var(--red);margin-bottom:18px;white-space:nowrap}
.feature p{font-size:11.5px;line-height:17px;color:#444;margin-bottom:10px}
.feature strong{color:var(--ink)}

/* steps */
.step{top:1290px;display:flex;gap:16px}
.step-icon{width:50px;height:46px;border:1px solid var(--green);display:flex;align-items:center;justify-content:center;background:var(--white)}
.step-name{font-family:"Jost",sans-serif;font-weight:500;font-size:16px;color:var(--ink)}
.step-rule{width:30px;height:1px;background:#333;margin:7px 0 9px}
.step-text{font-size:11px;line-height:17px;color:#777;white-space:nowrap}

/* trades band */
.band{left:0;top:1446px;width:1200px;height:415px;background:linear-gradient(100deg,#e9e6e1 0%,#b7b2aa 35%,#6e6a64 70%,#4d4a46 100%)}
.trades{left:160px;top:1584px;width:420px;height:277px;background:rgba(255,255,255,.92);border-top:8px solid var(--green);padding:22px 14px 0 14px}
.trades-title{font-size:20px;color:var(--ink)}
.trades-rule{width:34px;height:2px;background:#333;margin:8px 0 16px}
.trades table{width:100%;border-collapse:collapse;font-size:11.5px}
.trades th{text-align:left;font-family:"Jost",sans-serif;font-weight:600;font-size:13px;padding:0 0 8px 0}
.trades th::before{content:"";display:inline-block;width:6px;height:6px;background:var(--green);margin-right:9px;vertical-align:middle}
.trades td{padding:6px 0;border-top:1px solid #bdbdbd;color:#444}
.trades td.sym{font-weight:700;color:var(--ink)}
.trades td.gain{color:var(--green);font-weight:700}
.trades td.loss{color:var(--red);font-weight:700}

/* services */
.card{top:1982px;width:425px;height:114px;background:var(--white);border:1px solid #e2e2e2;padding:18px 20px;font-size:11px;line-height:17px;color:#777;overflow:hidden;box-shadow:0 1px 3px rgba(0,0,0,.08)}
.card-label{top:2113px;font-family:"Jost",sans-serif;font-weight:600;font-size:20px;color:var(--ink)}
.card-label small{font-weight:400;font-size:12px;margin-left:8px}
.card-arrow{width:28px;height:28px;border-radius:50%;border:1px solid #999;display:flex;align-items:center;justify-content:center;background:var(--white)}
.card-rule{top:2167px;height:2px;background:var(--line)}

/* footer */
.footer{left:0;top:2241px;width:1200px;height:189px;background:var(--footer)}
.footer-title{font-family:"Jost",sans-serif;font-size:15px;color:#dcdcdc}
.footer-list{list-style:none;font-size:11px;line-height:21px;color:#9a9a9a}
.footer-list li::before{content:"";display:inline-block;width:4px;height:4px;background:var(--green);border-radius:50%;margin-right:6px;vertical-align:middle}
.newsletter-input{left:815px;top:2296px;width:225px;height:35px;background:var(--white);border-radius:3px}
.btn-subscribe{left:815px;top:2347px;width:76px;height:29px;background:var(--green);color:var(--white);font-size:11px;display:flex;align-items:center;justify-content:center;border-radius:2px}
.footer-base{left:0;top:2430px;width:1200px;height:49px;background:var(--footer-base)}
.copyright{left:160px;top:2448px;font-size:11px;color:#a5a5a5}
.copyright b{color:var(--green);font-weight:400}
.social{left:952px;top:2441px;display:flex;gap:8px}
.social span{width:26px;height:26px;border-radius:50%;border:1.5px solid #cfcfcf}
</style>
</head>
<body>

<!-- Hero -->
<div class="abs hero" role="img" aria-label="Photo of hands holding a tablet showing stock market charts"></div>
<div class="abs logo">
  <span class="logo-mark"></span>
  <div class="logo-name">LumoFortunates</div>
</div>
<nav class="abs nav">
  <span class="nav-home"><svg width="22" height="20" viewBox="0 0 22 20"><path d="M11 1 1 10h3v9h5v-6h4v6h5v-9h3z" fill="#2fae4a"/></svg></span>
  <a class="active">About</a><a>How it works</a><a>Video</a><a>FAQ</a><a>Sign up</a>
</nav>
<div class="abs hero-box">
  <h1 class="heading hero-title">I turned the stock market into my source of income!</h1>
  <span class="hero-link">CLICK TO WATCH VIDEO</span>
</div>

<!-- What is -->
<h2 class="abs heading section-title" style="top:642px">What is <em>Tally?</em></h2>
<div class="abs divider" style="top:680px"></div>
<p class="abs intro">Did you know that today over 50 different companies on the stock market went up 20-300%? This happens every day and I can<br>show you how to turn the Stock Market into your own private business. My goal is to help you make more money.</p>
<div class="abs btn-outline">Get started today</div>

<!-- Video feature -->
<div class="abs video" role="img" aria-label="Video still of the mentor at a tennis stadium with arms open">
  <svg class="abs video-play" width="66" height="66" viewBox="0 0 66 66"><circle cx="33" cy="33" r="30" fill="none" stroke="#fff" stroke-width="3"/><path d="M26 20v26l21-13z" fill="#fff"/></svg>
  <div class="abs video-caption">I TURNED THE STOCK MARKET INTO MY SOURCE OF</div>
</div>
<div class="abs feature">
  <h3 class="heading feature-title">8 out of 10 of my alert go up 20% S.D</h3>
  <p><strong>Here is how you can benefit:</strong><br>I do the research and invest my own money, sending a text alert telling you what I just bought/sold.<br>This info, you may include in your own research or you may duplicate my trades.</p>
  <p>LumoFortunate's goal is to help those ready to become independent &amp; financially free, even if you are low on funds. He is posting 1-2 FREE Alerts weekly on our Chatterbook page.</p>
</div>

<!-- How it works -->
<h2 class="abs heading section-title" style="top:1204px">How <em>LumoFortunate</em> works?</h2>
<div class="abs divider" style="top:1243px"></div>

<div class="abs step" style="left:160px">
  <div class="step-icon"><svg width="28" height="22" viewBox="0 0 28 22" fill="none" stroke="#333" stroke-width="1.6"><rect x="3" y="2" width="22" height="5"/><rect x="2" y="8" width="24" height="5"/><rect x="3" y="14" width="22" height="5"/></svg></div>
  <div><div class="step-name">Step - 1</div><div class="step-rule"></div><div class="step-text">Get Text Alerts &amp; Education<br>&amp; LEARN MY 4 INDICATORS.</div></div>
</div>
<div class="abs step" style="left:484px">
  <div class="step-icon"><svg width="28" height="26" viewBox="0 0 28 26" fill="none" stroke="#333" stroke-width="1.6"><rect x="3" y="10" width="22" height="13"/><rect x="7" y="3" width="14" height="7"/><path d="M7 14h3M12 14h3M17 14h3M7 18h3M12 18h3M17 18h3"/></svg></div>
  <div><div class="step-name">Step - 2</div><div class="step-rule"></div><div class="step-text">Practice Live Trading<br>BUY AND SELL SAME DAY</div></div>
</div>
<div class="abs step" style="left:783px">
  <div class="step-icon"><svg width="28" height="22" viewBox="0 0 28 22" fill="none" stroke="#333" stroke-width="1.6"><rect x="2" y="6" width="20" height="12" transform="rotate(-12 12 12)"/><rect x="6" y="7" width="20" height="12"/><circle cx="16" cy="13" r="3"/></svg></div>
  <div><div class="step-name">Step - 3</div><div class="step-rule"></div><div class="step-text">Make Money<br>Sit back and wait for next opportunity</div></div>
</div>

<!-- Latest trades -->
<div class="abs band" role="img" aria-label="Photo of a hand holding a phone with a trading app beside a trade sign"></div>
<div class="abs trades">
  <h3 class="heading trades-title">LumoFortunate's lastest trades</h3>
  <div class="trades-rule"></div>
  <table>
    <thead><tr><th>Date</th><th>Stock</th><th>Entry</th><th>Exit</th><th>Profit</th></tr></thead>
    <tbody>
      <tr><td>8/29</td><td class="sym">BRQ</td><td>$ 0.43</td><td>$ 0.55</td><td class="gain">$ 1,4400.00</td></tr>
      <tr><td>8/28</td><td class="sym">MVLA</td><td>$ 0.31</td><td>$ 0.35</td><td class="gain">$ 1637.00</td></tr>
      <tr><td>8/28</td><td class="sym">DQTN</td><td>$ 0.12</td><td>$ 0.14</td><td class="gain">$ 1,416.00</td></tr>
      <tr><td>8/24</td><td class="sym">LXVR</td><td>$ 0.42</td><td>$ 0.37</td><td class="loss">$ (310.00)</td></tr>
      <tr><td>8/23</td><td class="sym">OPZN</td><td>$ 0.08</td><td>$ 0.12</td><td class="gain">$ 240.00</td></tr>
    </tbody>
  </table>
</div>

<!-- Alerts & Coach -->
<h2 class="abs heading section-title" style="top:1908px">Lumo Alerts &amp; Coach</h2>
<div class="abs card" style="left:160px">With LumoAlerts*** you know exactly when I get in and out of my trades. Take advantage of the Free Training class for subscribers, a great tool for new traders or those with some experience. You can expect 1-3 Alerts per day on Stocks under $10.</div>
<div class="abs card" style="left:615px">Is not about the Money. Is about your super power!<br>That's the secret you learn One on One with The LumoFortunate. With a personalized analysis covering the Law of Attraction in your life, LumoFortunate pinpoints the subconscious blocks that are holding you back from</div>
<div class="abs card-label" style="left:160px">LumoAlerts!<small>(MOST POPULAR SERVICE)</small></div>
<div class="abs card-arrow" style="left:553px;top:2124px"><svg width="8" height="10" viewBox="0 0 8 10"><path d="M2 1l4 4-4 4" fill="none" stroke="#333" stroke-width="1.5"/></svg></div>
<div class="abs card-label" style="left:615px">LumoCoach!</div>
<div class="abs card-arrow" style="left:1014px;top:2124px;border-color:#ccc"><svg width="8" height="10" viewBox="0 0 8 10"><path d="M2 1l4 4-4 4" fill="none" stroke="#aaa" stroke-width="1.5"/></svg></div>
<div class="abs card-rule" style="left:160px;width:880px"></div>
<div class="abs card-rule" style="left:160px;width:420px;background:var(--green)"></div>

<!-- Footer -->
<footer>
  <div class="abs footer"></div>
  <div class="abs footer-title" style="left:160px;top:2258px">Useful Links</div>
  <ul class="abs footer-list" style="left:160px;top:2288px"><li>Home</li><li>Contact Us</li><li>Disclaimer</li><li>Tips</li><li>Español</li></ul>
  <div class="abs footer-title" style="left:408px;top:2258px">Learn more about</div>
  <ul class="abs footer-list" style="left:408px;top:2288px"><li>About Us</li><li>FAQ</li><li>Sign Up</li><li>Help</li></ul>
  <ul class="abs footer-list" style="left:598px;top:2288px"><li>Terms and Condition</li><li>Privacy Policy</li></ul>
  <div class="abs footer-title" style="left:815px;top:2260px">Our Newsletter</div>
  <div class="abs newsletter-input"></div>
  <div class="abs btn-subscribe">Subscribe</div>
  <div class="abs footer-base"></div>
  <div class="abs copyright">Copyright © 2017 &nbsp;<b>LumoFortunates</b>&nbsp; All Rights Reserved &nbsp; / &nbsp; Privacy Policy</div>
  <div class="abs social" aria-label="Social links"><span></span><span></span><span></span></div>
</footer>

</body>
</html>
```